Business Card Design for a Lending Business (Hard Money loans)

We need a business card for our Real Estate Lending business. We do hard Money loans for real estate investors. We have an existing logo we like, see attached. I'd like the business card to mostly include the logo colors, but a bright color pop of some sort would be nice to see also. Card should include Logo, Company Name, Company Address, Employee Name, Cell Phone, Main Phone, Email, Website

Industry/Entity Type

Finance / Lending

Contact Information for Business Card

Logo, Company Name, Company Address, Employee Name, Cell Phone, Main Phone, Email, Website

Requirements
Nice to have
• I'd like the business card to mostly include the logo colors, but a bright color pop of some sort would be nice to see also.

```html
<!DOCTYPE html>
<html lang="en">
<head>
<meta charset="utf-8">
<title>Crestline Lending – Business Card</title>
<link rel="stylesheet" href="https://fonts.googleapis.com/css2?family=Montserrat:wght@400;500;700&display=swap">
<style>
  :root {
    --sky: #06ade0;
    --navy: #2b3a8c;
    --paper: #f4f5fa;
    --ink: #1d1d24;
    --backdrop: #2a2b2f;
    --white: #ffffff;
  }
  * { margin: 0; padding: 0; box-sizing: border-box; }
  html, body {
    width: 1200px; height: 900px; overflow: hidden;
    background: var(--backdrop);
    font-family: "Montserrat", sans-serif;
  }
  .canvas {
    width: 1200px; height: 900px;
    display: flex; flex-direction: column; align-items: center; justify-content: center;
    gap: 40px;
  }
  .card {
    position: relative;
    width: 700px; height: 400px;
    overflow: hidden;
    box-shadow: 0 14px 30px rgba(0,0,0,.45);
  }
  .card-front { background: var(--sky); display: flex; align-items: center; justify-content: center; }
  .card-back { background: var(--paper); }
  .card-back svg.wave { position: absolute; inset: 0; }

  .brand {
    display: flex; align-items: center; gap: 14px;
    color: var(--white);
    font-weight: 700; letter-spacing: 3px; text-transform: uppercase;
    white-space: nowrap;
  }
  .brand-dot { border-radius: 50%; background: var(--white); flex: none; }
  .brand-front { font-size: 34px; }
  .brand-front .brand-dot { width: 22px; height: 22px; }
  .brand-back { position: absolute; left: 50px; top: 120px; font-size: 24px; }
  .brand-back .brand-dot { width: 16px; height: 16px; }

  .address {
    position: absolute; left: 60px; top: 330px;
    font-size: 13px; line-height: 1.45; color: var(--ink);
  }
  .contact {
    position: absolute; right: 30px; top: 160px;
    text-align: right;
  }
  .person-name { font-size: 22px; font-weight: 700; color: var(--sky); white-space: nowrap; }
  .person-role { font-size: 12px; color: var(--ink); margin-bottom: 24px; }
  .contact-line {
    display: flex; align-items: center; justify-content: flex-end; gap: 10px;
    font-size: 12px; line-height: 19px; color: var(--ink); white-space: nowrap;
  }
  .contact-line svg { width: 12px; height: 12px; flex: none; fill: var(--sky); }
</style>
</head>
<body>
<main class="canvas">
  <section class="card card-front">
    <div class="brand brand-front"><span class="brand-dot"></span>Crestline Lending</div>
  </section>

  <section class="card card-back">
    <svg class="wave" viewBox="0 0 700 400" width="700" height="400">
      <path d="M0 0 H700 V94 C556 94 460 118 430 210 C400 300 350 314 270 314 C170 314 80 308 0 300 Z" fill="var(--navy)"/>
      <path d="M0 0 H700 V90 C560 90 470 110 440 200 C410 290 360 300 280 300 C170 300 80 295 0 285 Z" fill="var(--sky)"/>
    </svg>
    <div class="brand brand-back"><span class="brand-dot"></span>Crestline Lending</div>
    <p class="address">418 Harbor Ridge Ave, #112<br>Lakemont, OH 43990</p>
    <div class="contact">
      <div class="person-name">Jonah Perrault</div>
      <div class="person-role">Owner</div>
      <div class="contact-line">555-210-4817
        <svg viewBox="0 0 12 12"><path d="M2 1h3l1 3-2 1a7 7 0 0 0 3 3l1-2 3 1v3c-6 0-9-3-9-9z"/></svg></div>
      <div class="contact-line">555-210-4817
        <svg viewBox="0 0 12 12"><path d="M3 0h6a1 1 0 0 1 1 1v10a1 1 0 0 1-1 1H3a1 1 0 0 1-1-1V1a1 1 0 0 1 1-1zm0 2v7h6V2z"/></svg></div>
      <div class="contact-line">info@crestlinelending.com
        <svg viewBox="0 0 12 12"><path d="M0 2h12v8H0zM1 3l5 4 5-4z"/></svg></div>
      <div class="contact-line">www.crestlinelending.com
        <svg viewBox="0 0 12 12"><circle cx="6" cy="6" r="5.5"/></svg></div>
    </div>
  </section>
</main>
</body>
</html>
```